Holiday Rental Company Flyer Design (DL not A5)

Note from PixelFolk Administration: The category sizing selected is A5, however the project requires DL sized artwork. Please refer to the DL template link below while the 'Special Requirements' are updated accordingly.

Project Brief:
We need a double sided DL flyer designed for an up market Holiday Rental Company that portrays a personalised approach to property management. These are to be used for letter box drops to homes we're specifically targeting so the design should be modern, complimentary colour palette, uncluttered & visually appealing.

Please Download the DL Template from Quillmark here: http://www.quillmark.com.au/qm/ns/propath/UploadResources.aspx?selectedTab=0?pfid=BFB&pf_id=BFB&xnav=easypath-upload-image#Templates

Target Market(s)

Wealthy Home Owners

Industry/Entity Type

It Company

Font styles to use
Other font styles liked:
• Avant Garde Extra Light & Demi

Colors
33b8a4

Requirements
Must have
• DL Flyer sizes (210mm width x 99mm width, plus 3mm bleed)
• Front: Logo, Main Image & Grab
• Back: Contact Details & Brief Description of our business
• Images: Ideally the main image should be the house with the pool but alternatively a lifestyle images could also be used.
Nice to have
• A creative designer!
Should not have
• Clutter & busy designs

```html
<!DOCTYPE html>
<html lang="en">
<head>
<meta charset="utf-8">
<title>Harbourline Retreats – DL Flyer</title>
<link rel="stylesheet" href="https://fonts.googleapis.com/css2?family=Poppins:wght@200;300;600&display=swap">
<style>
  :root {
    --teal: #1fb39a;
    --teal-deep: #17a08a;
    --white: #ffffff;
    --text-soft: #d6f2ec;
    --backdrop: #ecebe8;
    --pool-dark: #1d1f3a;
    --pool-blue: #3a7fe0;
    --sea: #35c4d0;
    --bed-warm: #e8cfa2;
    --flower-warm: #c8a47c;
  }
  * { margin: 0; padding: 0; box-sizing: border-box; }
  html, body { width: 1200px; height: 1000px; overflow: hidden; }
  body {
    background: var(--backdrop);
    font-family: "Poppins", sans-serif;
    position: relative;
  }

  /* Front side */
  .flyer-front {
    position: absolute; left: 22px; top: 38px; width: 964px; height: 456px;
    background: var(--white);
  }
  .front-photo {
    position: absolute; left: 8px; top: 8px; width: 710px; height: 440px;
    background: linear-gradient(160deg, var(--pool-dark) 0%, #4a3f5e 45%, #2a4c8a 75%, var(--pool-blue) 100%);
  }
  .brand-panel {
    position: absolute; left: 460px; top: 52px; width: 496px; height: 352px;
    background: var(--teal);
  }
  .brand-frame {
    position: absolute; inset: 8px;
    border: 1px solid rgba(255,255,255,0.6);
  }
  .brand-name {
    position: absolute; left: 0; right: 0; top: 64px;
    text-align: center; color: var(--white);
    font-weight: 200; font-size: 44px; line-height: 1.28; letter-spacing: 3px;
  }
  .brand-tagline {
    position: absolute; left: 0; right: 0; top: 300px;
    text-align: center; color: var(--white);
    font-weight: 300; font-size: 16px; letter-spacing: 0.6px;
  }

  /* Back side */
  .flyer-back {
    position: absolute; left: 214px; top: 505px; width: 964px; height: 457px;
    background: var(--teal);
  }
  .back-copy {
    position: absolute; left: 66px; top: 26px; width: 560px;
    color: var(--text-soft); font-weight: 200; font-size: 14.5px; line-height: 24px;
  }
  .back-copy p { margin-bottom: 24px; }
  .back-copy .intro { margin-left: 4px; }
  .benefits { list-style: none; margin-bottom: 24px; }
  .benefits li { position: relative; padding-left: 26px; }
  .benefits li::before {
    content: ""; position: absolute; left: 2px; top: 7px;
    width: 10px; height: 10px; border: 1px solid var(--text-soft); border-radius: 50%;
  }
  .contact-list { list-style: none; color: var(--white); font-weight: 600; font-size: 15px; }
  .gallery {
    position: absolute; left: 662px; top: 0; width: 208px; height: 457px;
    background: var(--white);
  }
  .gallery-photo { position: absolute; left: 8px; width: 191px; }
  .photo-swim { top: 16px; height: 139px; background: linear-gradient(180deg, #5fd6de, var(--sea)); }
  .photo-bedroom { top: 160px; height: 138px; background: linear-gradient(135deg, var(--bed-warm), #d9b24a 55%, #e0705a); }
  .photo-flowers { top: 303px; height: 138px; background: linear-gradient(180deg, #8c8a86, var(--flower-warm)); }
  .pattern-strip {
    position: absolute; left: 870px; top: 0; width: 94px; height: 457px;
    background: linear-gradient(180deg, var(--teal), var(--teal-deep));
  }
</style>
</head>
<body>
  <section class="flyer-front">
    <div class="front-photo" role="img" aria-label="Night view of a modern luxury home with lit interiors beside a glowing blue swimming pool"></div>
    <div class="brand-panel">
      <div class="brand-frame"></div>
      <h1 class="brand-name">HARBOURLINE<br>RETREATS</h1>
      <p class="brand-tagline">Holiday Rental Management With A Difference.</p>
    </div>
  </section>

  <section class="flyer-back">
    <div class="back-copy">
      <p class="intro">What we do differently!</p>
      <p>Rather than relying upon a key safe or a central pick-up destination, a ‘Harbourline Retreats’ staff member will greet guests upon arrival.</p>
      <p style="margin-bottom:0">Our ‘Meet &amp; Greet’ service provides home owners with an increased level of Security and also allows us to:</p>
      <ul class="benefits">
        <li>Prepare the home for their arrival (lights, heaters, music etc.)</li>
        <li>Establish a rapport &amp; help facilitate future bookings</li>
        <li>Reiterate their responsibilities to ensure the return of their bond</li>
      </ul>
      <p style="margin-bottom:0">If you’d like to know what your property could achieve or require additional information, please contact us on:</p>
      <ul class="contact-list">
        <li>t: (03)5000 1742</li>
        <li>e: stay@harbourlineretreats.com.au</li>
        <li>w: harbourlineretreats.com.au</li>
        <li>PO Box 18, Seacove Victoria 3990</li>
      </ul>
    </div>
    <div class="gallery">
      <div class="gallery-photo photo-swim" role="img" aria-label="Dolphins swimming in clear turquoise water"></div>
      <div class="gallery-photo photo-bedroom" role="img" aria-label="Bedroom with yellow cushions and a colourful patterned quilt"></div>
      <div class="gallery-photo photo-flowers" role="img" aria-label="Bird of paradise flowers in a glass vase with candles"></div>
    </div>
    <div class="pattern-strip" role="img" aria-label="Decorative strip of repeating outlined floral pattern"></div>
  </section>
</body>
</html>
```